Glanvero foot health or foot health glanvero

Treatments in comfort of your own home
Delia Marsh cert KTRVb Pod, LQNDoct
Treatments will be listed on the leaflet I will attach
I am a Foot Health practitioner,
I want to mention I do home visits throughout Pembrokeshire & Ceredigion.
Tel. 07604519283
I have 2 logs to forward to you they are the associations I belong to .
One of which is also a certification mark. It is important that the same colour is used for this mark. They are not the main focus, they are just recognised mark. To be at the top or bottom of the page.
There is a local business called Tregarrow foot clinic, so my business has to be glanvero foot health, or foot health glanvero
soon I will also need a web page and cards designed, so please keep this in mind when designing the Artwork. I will also need an email on the leaflet but I will wait and see what the design is first before I confirm it as I have several.
I hope this is enough info for you.
Many thanks,
Delia Marsh

Target Market(s)

Mostly the elderly, some middle age women, but it is a service for all ages. The elderly are my main clients.

Industry/Entity Type

Health

Font styles to use
Serif
Sans Serif

Colors

Designer to choose colors to be used in the design.

Requirements
Must have
• Covering Pembrokeshire & Ceredigion.
Treatments include:- as listed on example leaflet I sent
Phone number a size that's easily readable.
I am open to colours. I love bright colours, but also like the more conservative colours as long as it looks professional. I'm wanting it to look more up market.
Nice to have
• Logo for Guildhall and KTE logo obviously smaller, but also recognisable and either at the top of page or bottom. These are not to be main focal point.

```html
<!DOCTYPE html>
<html lang="en">
<head>
<meta charset="utf-8">
<title>Glanvero Foot Health – Leaflet</title>
<link rel="stylesheet" href="https://fonts.googleapis.com/css2?family=Arimo:wght@400;700&family=Open+Sans:wght@300;400&display=swap">
<style>
  :root {
    --teal: #12adb5;
    --magenta: #c562a8;
    --magenta-deep: #b73a93;
    --plum: #8b2a78;
    --white: #ffffff;
    --skin-light: #f1d4bf;
    --skin-mid: #d9a889;
    --backdrop: #8d8580;
    --badge-purple: #6b2c91;
    --badge-red: #b8322e;
    --page: #ffffff;
  }
  * { margin: 0; padding: 0; box-sizing: border-box; }
  html, body {
    width: 1200px; height: 1000px; overflow: hidden;
    background: var(--page);
    font-family: "Arimo", Arial, sans-serif;
  }
  .leaflet {
    position: absolute; left: 290px; top: 58px;
    width: 622px; height: 882px;
    background: var(--white);
    overflow: hidden;
  }
  .brand {
    position: absolute; left: 38px; top: 60px;
    display: flex; align-items: center; gap: 10px;
    color: var(--plum); font-size: 21px; font-weight: 400;
  }
  .brand-dot {
    width: 12px; height: 12px; border-radius: 50%;
    background: var(--plum);
  }
  .headline-box {
    position: absolute; left: 310px; top: 0;
    width: 312px; height: 129px;
    background: var(--teal);
    color: var(--white);
    font-size: 30px; font-weight: 700; line-height: 35px;
    padding: 12px 0 0 20px;
  }
  .hero {
    position: absolute; left: 0; top: 140px;
    width: 622px; height: 637px;
  }
  .hero svg { display: block; }
  .treatments {
    position: absolute; left: 50px; top: 346px;
    color: var(--white);
  }
  .treatments-intro {
    font-family: "Open Sans", Arial, sans-serif;
    font-weight: 400; font-size: 16px;
    margin-left: 30px; margin-bottom: 18px;
  }
  .treatment-list { list-style: none; }
  .treatment-list li {
    display: flex; align-items: center; gap: 14px;
    font-size: 22px; font-weight: 700;
    height: 44.5px;
  }
  .treatment-list li::before {
    content: ""; width: 14px; height: 14px; border-radius: 50%;
    border: 2px solid var(--white);
  }
  .coverage {
    position: absolute; left: 50px; top: 680px;
    color: var(--white); font-size: 16px; font-weight: 700;
  }
  .phone {
    position: absolute; left: 48px; top: 709px;
    color: var(--white);
    font-family: "Open Sans", Arial, sans-serif;
    font-weight: 300; font-size: 40px; letter-spacing: 1px;
  }
  .practitioner {
    position: absolute; left: 0; top: 791px;
    width: 310px; height: 91px;
    background: var(--teal); color: var(--white);
    padding: 26px 0 0 50px;
    font-family: "Open Sans", Arial, sans-serif;
    font-size: 14px; line-height: 26px;
  }
  .practitioner .credentials { font-size: 9px; }
  .memberships {
    position: absolute; left: 352px; top: 806px;
    display: flex; align-items: center; gap: 36px;
  }
  .badge-register {
    width: 112px; height: 40px; border-radius: 4px;
    background: var(--badge-purple);
  }
  .badge-guild {
    width: 60px; height: 60px; border-radius: 50%;
    background: var(--badge-red);
  }
</style>
</head>
<body>
  <main class="leaflet">
    <div class="brand">
      <span class="brand-dot"></span>
      <span class="brand-name">Glanvero Foot Health</span>
    </div>

    <h1 class="headline-box">Foot Treatments in the comfort of your own home</h1>

    <section class="hero">
      <svg width="622" height="637" viewBox="0 0 622 637">
        <defs>
          <linearGradient id="photoTone" x1="0" y1="0" x2="1" y2="1">
            <stop offset="0" stop-color="var(--backdrop)"/>
            <stop offset="0.45" stop-color="var(--skin-mid)"/>
            <stop offset="0.8" stop-color="var(--skin-light)"/>
            <stop offset="1" stop-color="#e9e2dd"/>
          </linearGradient>
        </defs>
        <rect class="hero-photo" width="622" height="637" fill="url(#photoTone)"
              role="img" aria-label="Photograph of a hand massaging the sole of a bare foot"/>
        <path class="hero-curve-teal" d="M0,0 L60,0 C350,60 560,330 622,637 L0,637 Z" fill="var(--teal)"/>
        <path class="hero-curve-magenta" d="M0,72 C250,100 480,300 560,637 L0,637 Z" fill="var(--magenta)"/>
      </svg>
    </section>

    <section class="treatments">
      <p class="treatments-intro">Treatments include:</p>
      <ul class="treatment-list">
        <li>Diabetic Foot Care</li>
        <li>Ingrowing Toenails</li>
        <li>Corn &amp; Callous Treatment</li>
        <li>Toenail Clipping</li>
        <li>Fungal Infections Treated</li>
        <li>Cracked Heels</li>
      </ul>
    </section>

    <p class="coverage">We do home visits throughout Pembrokeshire &amp; Ceredigion</p>
    <p class="phone">Tel: 07604 519283</p>

    <footer>
      <div class="practitioner">
        <p>Delia Marsh <span class="credentials">cert KTRVb Pod, LQNDoct</span></p>
        <p>Foot Health Practitioner</p>
      </div>
      <div class="memberships">
        <div class="badge-register" role="img" aria-label="KTE accredited register certification mark"></div>
        <div class="badge-guild" role="img" aria-label="Guildhall practitioners association badge"></div>
      </div>
    </footer>
  </main>
</body>
</html>
```